International business needs business cards

Our company, RUV Partners Inc. is in the business of supplying a range construction products with particular emphasis on CEMENT. We have developed our own brand - BOREAL SUPPLIES - with which to infiltrate the market. We are launching our brand of cement (BOREAL Type IS Cement) into the Caribbean which is unlike anything this market has ever seen. A monopoly has existed here for the past 60-odd years and the market has now opened to allow the importation of other brands and consumers are anxious and ready for change/improvement. We are very excited to be launching and want to make a great first impression. We will be conducting workshops and seminars (from government level to the hardware store owners) and we want our business card to give us the strong, confident introduction that we need.

Target Market(s)

construction; builders; engineers; home owners

Industry/Entity Type

Construction

Contact Information for Business Card

Melvina Tosh
CEO
cell # 1 868 5550147
Ground floor,Palmetto Plaza Suite 2473
George Town,Grand Cayman
Cayman Islands,KY1-1990
EMAIL: m.tosh@ruvpartnersinc.example
web site ruvpartnersinc.example

COMPANY: skype info ruv.partners.example

second card
Hester Quimby-Tosh
CFO
CELL# 1 868 555 0382
George Town,Grand Cayman
Cayman Islands,KY1-1990
EMAIL: h.quimbytosh@ruvpartnersinc.example
website ruvpartnersinc.example

Requirements
Must have
• Business cards must display BOTH logos - RUV is the company and BOREAL is the brand.

```html
<!DOCTYPE html>
<html lang="en">
<head>
<meta charset="utf-8">
<title>RUV Partners Inc. – Business Card</title>
<link rel="stylesheet" href="https://fonts.googleapis.com/css2?family=Noto+Sans:wght@400;700&display=swap">
<style>
  :root {
    --backdrop: #efece6;
    --card-white: #ffffff;
    --brand-maroon: #7e161b;
    --ink: #111111;
    --ink-soft: #3a3a3a;
    --on-maroon: #ffffff;
    --card-edge: #d6d2cb;
  }
  * { margin: 0; padding: 0; box-sizing: border-box; }
  html, body {
    width: 1189px; height: 1200px; overflow: hidden;
    background: var(--backdrop);
    font-family: "Noto Sans", Verdana, sans-serif;
  }
  .card {
    position: absolute;
    left: 171px;
    width: 856px;
    height: 488px;
    background: var(--card-white);
    border: 1px solid var(--card-edge);
    overflow: hidden;
  }
  .card--front { top: 67px; }
  .card--back { top: 626px; }

  /* front: company side */
  .company-mark {
    position: absolute;
    left: 48px; top: 175px;
    display: flex; align-items: center; gap: 16px;
  }
  .company-mark__square {
    width: 140px; height: 137px;
    background: var(--brand-maroon);
  }
  .company-mark__name {
    font-weight: 700;
    font-size: 26px;
    line-height: 1.15;
    color: var(--ink);
    width: 210px;
  }

  /* front: contact panel */
  .contact-panel {
    position: absolute;
    left: 428px; top: 0;
    width: 428px; height: 100%;
    background: var(--brand-maroon);
    color: var(--on-maroon);
    padding: 0 0 0 37px;
  }
  .contact-panel__name {
    position: absolute; left: 37px; top: 50px;
    font-size: 33px; font-weight: 700; line-height: 1.2;
  }
  .contact-panel__role {
    position: absolute; left: 37px; top: 91px;
    font-size: 23px; font-weight: 400; color: var(--ink);
  }
  .contact-panel__address {
    position: absolute; left: 37px; top: 159px;
    font-size: 22px; line-height: 29px; font-style: normal;
  }
  .contact-list {
    position: absolute; left: 37px; top: 288px;
    list-style: none;
  }
  .contact-list__item {
    display: flex; align-items: center; gap: 6px;
    height: 28px; margin-bottom: 5px;
    font-size: 22px;
  }
  .contact-list__icon {
    width: 28px; height: 28px;
    background: var(--ink);
    display: flex; align-items: center; justify-content: center;
  }
  .contact-panel__web {
    position: absolute; left: 37px; top: 393px;
    font-size: 22px; color: var(--ink);
  }

  /* back: brand side */
  .brand-mark {
    position: absolute;
    left: 50%; top: 50%;
    transform: translate(-50%, -50%);
    display: flex; flex-direction: column; align-items: center; gap: 14px;
  }
  .brand-mark__circle {
    width: 150px; height: 150px; border-radius: 50%;
    background: var(--ink-soft);
  }
  .brand-mark__name {
    font-size: 26px; font-weight: 700; letter-spacing: 6px;
    color: var(--ink-soft);
  }
</style>
</head>
<body>
  <section class="card card--front">
    <div class="company-mark">
      <div class="company-mark__square"></div>
      <div class="company-mark__name">RUV Partners Inc.</div>
    </div>

    <div class="contact-panel">
      <h1 class="contact-panel__name">Melvina Tosh</h1>
      <p class="contact-panel__role">CEO</p>
      <address class="contact-panel__address">
        Ground floor<br>
        Palmetto Plaza Suite 2473<br>
        George Town,Grand Cayman<br>
        Cayman Islands,KY1-1990
      </address>
      <ul class="contact-list">
        <li class="contact-list__item">
          <span class="contact-list__icon">
            <svg width="14" height="22" viewBox="0 0 14 22" aria-hidden="true">
              <rect x="1" y="1" width="12" height="20" rx="2" fill="none" stroke="#fff" stroke-width="1.6"/>
              <rect x="3" y="3.5" width="8" height="6" fill="#fff"/>
              <g fill="#fff"><rect x="3" y="12" width="2" height="2"/><rect x="6" y="12" width="2" height="2"/><rect x="9" y="12" width="2" height="2"/><rect x="3" y="15.5" width="2" height="2"/><rect x="6" y="15.5" width="2" height="2"/><rect x="9" y="15.5" width="2" height="2"/></g>
            </svg>
          </span>
          1 868 5550147
        </li>
        <li class="contact-list__item">
          <span class="contact-list__icon">
            <svg width="22" height="16" viewBox="0 0 22 16" aria-hidden="true">
              <rect x="1" y="1" width="20" height="14" fill="none" stroke="#fff" stroke-width="1.6"/>
              <path d="M1 1 L11 9 L21 1 M1 15 L8 7 M21 15 L14 7" fill="none" stroke="#fff" stroke-width="1.6"/>
            </svg>
          </span>
          m.tosh@ruvpartnersinc.example
        </li>
        <li class="contact-list__item">
          <span class="contact-list__icon"></span>
          ruv.partners.example
        </li>
      </ul>
      <p class="contact-panel__web">ruvpartnersinc.example</p>
    </div>
  </section>

  <section class="card card--back">
    <div class="brand-mark">
      <div class="brand-mark__circle"></div>
      <div class="brand-mark__name">BOREAL</div>
    </div>
  </section>
</body>
</html>
```